Web site for small printshop

I am looking for a website for small printshop in Iceland, mainly serving university students and artist.

We print posters, flyers, business cards and more.

In addition to our current website, I would like to include design tool, (fx. www.quarvelink.com, www.tandorizo.com or something similar) jobs upload, shopping chart.
Updates

Great work, I am really amazed of the quality of work i am seeing here.

Really way beyond my expectation

GOOD JOB - all of you ! 

Hi all.

The designs submitted have been great, way better than expected.
I really did not expect this level of quality.

Some have been asking me for feedback on their designs, and I will try 
to send some feedback here, without spoiling your creativity.

Likes:
- when the colors of my logo is used in menus, buttons etc.
- simple, not to crowded look.

Dislikes.
- Dark and heavy design
- Lot of text and buttons (crowded look)

Extra info.
- top line (before menus) will contain: Tel - email - language
- menu line will have 5 categories: Home - service - submission of works - FAQ - about us
- 3 large buttons:  Job submit - Job design - ask for offer

LOVE YOUR WORK - great designs so far :)

Target Market(s)

University Students, Artists. Age group 20-30

Industry/Entity Type

University

Requirements
Must have
• The website must be easy to use, clean looking.

```html
<!DOCTYPE html>
<html lang="en">
<head>
<meta charset="utf-8">
<title>Prentstofa – Printing like real</title>
<link rel="stylesheet" href="https://fonts.googleapis.com/css2?family=Arimo:wght@400;700&family=Tinos&display=swap">
<style>
:root{
  --paper:#efefea;
  --ink:#1d1d1d;
  --red:#e8403a;
  --green:#13622c;
  --rule:#d9d9d3;
  --dark:#262626;
  --muted:#8a8a86;
}
*{margin:0;padding:0;box-sizing:border-box}
html,body{width:882px;height:1200px;overflow:hidden;background:var(--paper)}
body{font-family:"Arimo",Arial,sans-serif;color:var(--ink);position:relative}
.abs{position:absolute}

.topbar{left:0;top:0;width:882px;height:76px;background:linear-gradient(#fafafa,#e9e9e6);box-shadow:0 1px 3px rgba(0,0,0,.08)}
.brand{left:73px;top:25px;display:flex;align-items:center;gap:7px}
.brand-mark{width:23px;height:23px;background:var(--red)}
.brand-name{font-weight:700;font-size:19px;letter-spacing:.2px}
.main-nav a{position:absolute;top:35px;font-weight:700;font-size:16px;color:var(--ink);text-decoration:none}
.nav-active{left:279px;top:77px;width:99px;height:7px;background:var(--red)}

.hero-sky{left:560px;top:0;width:322px;height:240px;background:radial-gradient(ellipse at 70% 40%,rgba(170,200,225,.55),rgba(239,239,234,0) 70%)}
.hero-title{left:166px;top:164px;font-size:47px;line-height:1;letter-spacing:.5px}
.hero-like{left:348px;top:214px;font-size:14px;color:var(--green)}
.hero-real{left:166px;top:228px;font-size:31px;color:var(--red)}
.hero-photo{left:437px;top:88px;width:281px;height:258px;background:linear-gradient(180deg,#3f6b91 0%,#2a3c50 45%,#151515 100%);border-radius:110px 110px 0 0}

.rule{height:1px;background:var(--rule)}
.sub-nav{font-size:13px;top:368px}
.sub-nav span{position:absolute;top:0}

h2{font-weight:400}
.section-title{font-size:18px;top:420px;left:131px}
.story-icon{left:190px;top:447px;width:94px;height:108px;background:linear-gradient(135deg,#6e6e6e,#1f1f1f);transform:rotate(-14deg);border:5px solid #f4f4f4;box-shadow:0 3px 6px rgba(0,0,0,.3)}
.body-copy{font-size:9.5px;line-height:15px}
.center-title{width:882px;text-align:center;left:0;font-size:18px;color:var(--green)}

.step-u{left:166px;top:684px;font-size:60px;color:var(--red);line-height:1}
.step-upload{left:219px;top:693px;font-weight:700;font-size:12px}
.step-upload small{display:block;font-family:"Tinos",serif;font-weight:400;font-size:8px;color:var(--muted)}
.step-select{left:327px;top:690px;font-size:18px}
.step-select em{font-style:normal;color:var(--red);font-size:13px}
.size-select{left:326px;top:717px;width:142px;height:30px;border:1px solid #cfcfca;background:#f6f6f3;font-size:10px;display:flex;align-items:center;justify-content:center;color:#444}
.size-select svg{position:absolute;right:10px;top:11px}
.step-pay{left:513px;top:733px;font-size:12px}

.corner-dark{left:137px;top:850px;width:52px;height:58px;background:var(--dark)}
.corner-red{left:692px;top:1024px;width:52px;height:59px;background:var(--red)}
.card{left:152px;top:866px;width:577px;height:202px;background:#fff;box-shadow:0 2px 6px rgba(0,0,0,.12)}
.card-image{left:33px;top:29px;width:155px;height:150px;background:linear-gradient(160deg,#dfe6ec,#2c8fd6 55%,#1f2a33);border-radius:8px}
.card-title{left:217px;top:38px;font-size:18px}
.card-copy{left:215px;top:82px;width:325px;font-size:9.5px;line-height:15.5px}

.footer{left:0;width:882px;text-align:center;top:1159px;font-size:7px;font-weight:700}
.footer em{font-style:normal;color:var(--red)}
</style>
</head>
<body>
<header>
  <div class="abs topbar"></div>
  <div class="abs brand"><span class="brand-mark"></span><span class="brand-name">PRENTSTOFA</span></div>
  <nav class="main-nav">
    <a style="left:305px">HOME</a>
    <a style="left:403px">ABOUT US</a>
    <a style="left:513px">PORTOFOLIO</a>
    <a style="left:644px">CONTACT US</a>
  </nav>
  <div class="abs nav-active"></div>
</header>

<section class="hero">
  <div class="abs hero-sky"></div>
  <h1 class="abs hero-title" style="font-weight:400">PRINTING</h1>
  <span class="abs hero-like">LIKE</span>
  <span class="abs hero-real">REAL</span>
  <div class="abs hero-photo" role="img" aria-label="Man in a dark suit holding a printed portrait poster in front of his face"></div>
</section>

<div class="abs rule" style="left:131px;top:346px;width:585px"></div>
<nav class="abs sub-nav" style="left:0;width:882px">
  <svg class="abs" style="left:169px;top:-6px" width="20" height="20" viewBox="0 0 20 20"><path d="M10 1 L19 10 H16 V19 H4 V10 H1 Z" fill="#e8403a"/></svg>
  <span style="left:207px">HOME</span>
  <span style="left:300px">CATOGOREY</span>
  <span style="left:451px">ABOUT US</span>
  <span style="left:574px">BUY ONLINE</span>
</nav>
<div class="abs rule" style="left:131px;top:401px;width:585px"></div>

<section class="story">
  <h2 class="abs section-title">STORY BOARD</h2>
  <div class="abs story-icon" role="img" aria-label="Tilted photo print icon"></div>
  <p class="abs body-copy" style="left:315px;top:462px;width:375px">Bun Barn sprouted from a hot dog cart in Linden Square Park in Harborview created by Tomas Reyl's Civic Square Dining Group (CSDG) to support the Linden Square Park Conservancy's first art installation. The cart was quite the success, with Barn Fans lined up daily for three summers.</p>
</section>

<div class="abs rule" style="left:131px;top:566px;width:585px"></div>
<h2 class="abs center-title" style="top:586px">HOW CAN YOU CONTACT US</h2>
<div class="abs rule" style="left:131px;top:625px;width:585px"></div>

<section class="steps">
  <span class="abs step-u">U</span>
  <div class="abs step-upload">PLOAD<small>YOUR FILES</small></div>
  <svg class="abs" style="left:238px;top:716px" width="72" height="32" viewBox="0 0 72 32"><path d="M2 10 H44 V2 L70 16 L44 30 V22 H2 Z" fill="none" stroke="#222" stroke-width="3" stroke-linejoin="round"/><path d="M10 10 V22 M18 10 V22 M26 10 V22" stroke="#222" stroke-width="3"/></svg>
  <div class="abs step-select">SELECT <em>THE SIZE</em></div>
  <div class="abs size-select">A3<svg width="10" height="6" viewBox="0 0 10 6"><path d="M1 1 L5 5 L9 1" fill="none" stroke="#333" stroke-width="1.5"/></svg></div>
  <svg class="abs" style="left:483px;top:695px" width="43" height="19" viewBox="0 0 43 19"><path d="M1 6 H27 V1 L42 9.5 L27 18 V13 H1 Z" fill="none" stroke="#222" stroke-width="2" stroke-linejoin="round"/></svg>
  <svg class="abs" style="left:649px;top:676px" width="44" height="44" viewBox="0 0 44 44"><circle cx="22" cy="22" r="21" fill="#e8403a"/><path d="M12 22 L19 29 L32 14" fill="none" stroke="#fff" stroke-width="4.5" stroke-linecap="round" stroke-linejoin="round"/></svg>
  <span class="abs step-pay">AND PAY THE LOWEST COST</span>
</section>

<div class="abs rule" style="left:131px;top:790px;width:585px"></div>
<h2 class="abs center-title" style="top:812px">3: OUR SELECTING USED PRINTER</h2>

<section class="printer">
  <div class="abs corner-dark"></div>
  <div class="abs corner-red"></div>
  <div class="abs card">
    <div class="abs card-image" role="img" aria-label="Blue and black desktop inkjet printer with paper"></div>
    <h2 class="abs card-title">STORY BOARD</h2>
    <p class="abs card-copy">Bun Barn sprouted from a hot dog cart in Linden Square Park in Harborview created by Tomas Reyl's Civic Square Dining Group (CSDG) to support the Linden Square Park Conservancy's first art installation. The cart was quite the success, with Barn Fans lined up daily for three summers.</p>
  </div>
</section>

<div class="abs rule" style="left:353px;top:1140px;width:198px"></div>
<footer class="abs footer">ALLRIGHTS RESERVED BY <em>COMPANY NAME</em>@THE DATE</footer>
</body>
</html>
```